Vostrel Holdings Web Design

Vostrel Holdings Limited Shenzhen

This project is a 10 page launch website.
Our client is seeking a contemporary homepage design for a Holdings company. Once we are happy with the homepage design and select designer we will request a secondary page design.

Please see attached company LOGO for an idea of style, it incorporates the traditional Chinese furniture lattice work. The Quillmoor website is one of our clients favorite so we would like to see a similar homepage design to this website.

Use the websites below for reference purpose. The first two are Chinese and the second two are international. We would like to see elements of both but more focus on international design.

http://www.evergrande.com/http://www.brevandgroup.com/pub/default.aspx http://www.quillmoor.com/zh/maldives_resortone/
http://www.vellune-studio.com
http://media-cache-ec0.fotrelix.com/originals/41/a3/90/41a390c1f5b7d2e8a6c4f0b9e3d71a55.jpg

Company Background
VOSTREL HOLDINGS, located in Qianhai, China, is a new real-estate project operator, structuring urban-rural real-estate investment and development, and industrial fund investment. The company also invests in supply chain management and supporting infrastructures. To create new spaces and livable cities Vostrel Holdings develop win-win strategic partnerships with a number of institutions. Currently cooperating with Harrow East Lindcombe, China urban and rural integrated demonstration.

Target Market(s)

B2B property investment. Target market customers are senior level management/decision makers of large corporations. Focusing geographically on the domestic market first and expanding internationally in 2nd and 3rd years.

Industry/Entity Type

Investment

Requirements
Must have
• Since this is a new company, we would like to the website representing growth and power, E.g. like a growing tree.
Should not have
• Low-level vectors such as curency symbols, American dollar.

```html
<!DOCTYPE html>
<html lang="en">
<head>
<meta charset="utf-8">
<title>Vostrel Holdings</title>
<link href="https://fonts.googleapis.com/css2?family=Open+Sans:ital,wght@0,400;0,600;0,700;1,400;1,600&display=swap" rel="stylesheet">
<style>
:root{
  --gold:#d3a940;
  --gold-text:#c9a13a;
  --gold-dark:#a88327;
  --header:#141414;
  --ink:#555;
  --rule:#dedede;
  --footer:#2d2d2d;
  --footer-base:#232323;
  --white:#fff;
}
*{margin:0;padding:0;box-sizing:border-box}
html,body{width:737px;height:1200px;overflow:hidden;background:#fff;font-family:"Open Sans",Arial,sans-serif}
.page{position:relative;width:737px;height:1200px}

.site-header{position:absolute;left:0;top:0;width:737px;height:127px;background:linear-gradient(#1e1e1e,#0c0c0c)}
.brand{position:absolute;left:55px;top:10px;width:140px;text-align:center}
.brand-mark{display:block;margin:0 auto 6px;width:70px;height:70px;border-radius:50%;border:2px solid var(--gold)}
.brand-name{color:var(--gold);font-size:14.5px;font-weight:400;letter-spacing:.3px;white-space:nowrap}
.lang{position:absolute;top:39px;width:14px;height:10px}
.lang-cn{left:511px;background:#c8231c}
.lang-en{left:535px;background:#233b7a}
.search{position:absolute;left:558px;top:35px;width:118px;height:20px;background:#fff;border:1px solid #ccc;font-size:8px;color:#888;padding:4px 0 0 8px}
.search svg{position:absolute;right:6px;top:4px}
.main-nav{position:absolute;top:95px;left:333px;display:flex}
.main-nav a{color:#fff;text-decoration:none;font-size:8.5px;font-weight:600;height:18px;line-height:18px;padding:0 7px;margin-right:9px}
.main-nav a.active{background:var(--gold);color:#222;border-radius:2px}

.hero{position:absolute;left:0;top:127px;width:737px;height:365px;background:linear-gradient(#cfdbe6 0%,#e6e4dc 45%,#9b8572 75%,#3b3a3e 100%)}
.quote-box{position:absolute;left:480px;top:52px;width:196px;height:255px;background:rgba(40,40,40,.82);padding:16px 16px}
.quote-text{color:#fff;font-style:italic;font-weight:600;font-size:10.3px;line-height:18px}
.quote-author{color:var(--gold);font-style:italic;font-weight:600;font-size:10px;margin-top:10px}
.quote-rule{height:1px;background:rgba(255,255,255,.25);margin:18px -2px 13px}
.cta{display:block;width:156px;height:29px;margin-left:4px;background:linear-gradient(#e2bb55,#b88f2c);color:#2a2108;font-size:11px;font-weight:700;text-align:center;line-height:29px;border-radius:2px}
.dots{position:absolute;left:551px;top:419px;display:flex;gap:6px}
.dots span{width:8px;height:8px;border-radius:50%;background:#bbb;border:1px solid #666}

.service{position:absolute;top:515px;width:200px}
.service svg{position:absolute;left:0;top:3px}
.service h3{margin-left:46px;color:var(--gold-text);font-size:14px;font-weight:600;line-height:16px;white-space:nowrap}
.service p{margin-left:46px;margin-top:6px;width:140px;color:#666;font-size:7.8px;line-height:13px}
.rule{position:absolute;left:61px;width:615px;height:1px;background:var(--rule)}

.about h2{position:absolute;left:69px;top:624px;color:var(--gold-text);font-size:14px;font-weight:600}
.about p{position:absolute;left:69px;top:648px;width:397px;color:var(--ink);font-size:8.1px;line-height:15.4px;text-align:justify}
.about-photo{position:absolute;left:479px;top:627px;width:190px;height:95px;background:linear-gradient(#1c2948,#3a3f5c 55%,#6d5a3e)}

.partners{position:absolute;left:71px;top:772px;width:595px;display:flex;justify-content:space-between;align-items:center;color:#888;font-size:12px}
.partners span{font-weight:400}

.projects{position:absolute;left:0;top:812px;width:737px;height:246px;background:var(--gold)}
.projects h2{text-align:center;color:#fff;font-size:14px;font-weight:600;margin-top:18px}
.tile{position:absolute;width:140px;height:80px;border:3px solid #fff}

.site-footer{position:absolute;left:0;top:1058px;width:737px;height:104px;background:var(--footer)}
.footer-col h4{position:absolute;top:16px;color:var(--gold);font-size:10px;font-weight:400}
.footer-links{position:absolute;top:41px;list-style:none;font-size:8px;color:#ddd;line-height:15.4px}
.footer-divider{position:absolute;top:12px;width:1px;height:80px;background:#4a4a4a}
.social{position:absolute;font-size:8.2px;color:#ddd;display:flex;align-items:center;gap:7px}
.social i{width:16px;height:16px;border-radius:50%;background:#fff;display:block}
.copyright{position:absolute;left:0;top:1162px;width:737px;height:38px;background:var(--footer-base);color:#999;font-size:7.5px;text-align:center;line-height:38px}
</style>
</head>
<body>
<div class="page">

<header class="site-header">
  <div class="brand">
    <span class="brand-mark"></span>
    <div class="brand-name">VOSTREL HOLDINGS</div>
  </div>
  <span class="lang lang-cn"></span>
  <span class="lang lang-en"></span>
  <div class="search">Search
    <svg width="10" height="10" viewBox="0 0 10 10"><circle cx="4" cy="4" r="3" fill="none" stroke="#222" stroke-width="1.5"/><line x1="6" y1="6" x2="9.3" y2="9.3" stroke="#222" stroke-width="1.8"/></svg>
  </div>
  <nav class="main-nav">
    <a class="active">HOME</a><a>ABOUT US</a><a>SERVICES</a><a>PROJECTS</a><a>BLOG</a><a>CONTACT US</a>
  </nav>
</header>

<section class="hero" role="img" aria-label="Photo of a city skyline with a tall broadcast tower across a river at dusk">
  <div class="quote-box">
    <p class="quote-text">“ Nullam tincidunt lectus id est sollicitudin, at pretium arcu portti tor. Cras posuere, felis dignis sim luctus, sem urna semper leo, nec vehicula sapien dui id lectus. Nam vel quam sodales, vestibulum magna sed, dapibus est. ”</p>
    <p class="quote-author">Client name, City</p>
    <div class="quote-rule"></div>
    <span class="cta">CONTACT US NOW</span>
  </div>
</section>
<div class="dots"><span></span><span></span><span></span><span></span></div>

<div class="service" style="left:62px">
  <svg width="38" height="36" viewBox="0 0 38 36"><path d="M19 2 L2 18 H7 V34 H16 V24 H22 V34 H31 V18 H36 Z" fill="#d3a940"/></svg>
  <h3>REAL ESTATE</h3>
  <p>Quisque ullamcorper nisl pretium, mattis sapien a, fermentum nisi. In ornare quam ipsum ac.</p>
</div>
<div class="service" style="left:274px">
  <svg width="34" height="34" viewBox="0 0 34 34"><circle cx="17" cy="17" r="15" fill="none" stroke="#d3a940" stroke-width="3"/><circle cx="17" cy="17" r="10" fill="#d3a940"/><path d="M11 22 L15.5 17 L18.5 19.5 L23 13.5 M19.5 13 H23.5 V17" fill="none" stroke="#fff" stroke-width="1.8" stroke-linejoin="round"/></svg>
  <h3>INVESTMENT</h3>
  <p>Quisque ullamcorper nisl pretium, mattis sapien a, fermentum nisi. In ornare quam ipsum ac.</p>
</div>
<div class="service" style="left:481px">
  <svg width="34" height="36" viewBox="0 0 34 36"><rect x="12" y="1" width="10" height="8" fill="#d3a940"/><path d="M17 9 V15 M5 23 V15 H29 V23 M17 15 V23" stroke="#d3a940" stroke-width="3" fill="none"/><rect x="0" y="23" width="10" height="8" fill="#d3a940"/><rect x="12" y="23" width="10" height="8" fill="#d3a940"/><rect x="24" y="23" width="10" height="8" fill="#d3a940"/></svg>
  <h3 style="margin-left:44px">CHAIN MANAGEMENT</h3>
  <p style="margin-left:44px">Quisque ullamcorper nisl pretium, mattis sapien a, fermentum nisi. In ornare quam ipsum ac.</p>
</div>

<div class="rule" style="top:599px"></div>

<section class="about">
  <h2>ABOUT VOSTREL HOLDINGS</h2>
  <p>VOSTREL HOLDINGS, located in Qianhai, China, is a new real-estate project operator, structuring urban-rural real-estate investment and development, and industrial fund investment. The company also invests in supply chain management and supporting infrastructures. To create new spaces and livable cities Vostrel Holdings develop win-win strategic partnerships with a number of institutions. Currently cooperating with Harrow East Lindcombe, China urban and rural integrated demonstration.</p>
  <div class="about-photo" role="img" aria-label="Photo of illuminated city towers at night"></div>
</section>

<div class="rule" style="top:753px"></div>

<div class="partners">
  <span>Marlowe</span><span>Quorvia</span><span>Netbridge</span><span>Corvel</span><span>Hyrova</span><span>Tenra</span><span>Dalvent</span><span>Arlo</span><span>Sorvix</span>
</div>

<section class="projects">
  <h2>OUR PROJECTS</h2>
</section>
<div class="tile" style="left:67px;top:863px;background:linear-gradient(#9a9ea3,#3a3a3a)" role="img" aria-label="Photo of dancers with red fans on a riverside at sunset"></div>
<div class="tile" style="left:221px;top:863px;background:linear-gradient(#7fb0dc,#b9c6cf 55%,#4d6e3c)" role="img" aria-label="Photo of a harbour city skyline seen from a hill"></div>
<div class="tile" style="left:376px;top:863px;background:linear-gradient(#8fb7df,#b5443a 50%,#5b5046)" role="img" aria-label="Photo of a bronze guardian statue before a palace roof"></div>
<div class="tile" style="left:530px;top:863px;background:linear-gradient(#7a6a58,#b18b52 50%,#3a3535)" role="img" aria-label="Aerial photo of a city at dusk"></div>
<div class="tile" style="left:67px;top:960px;background:linear-gradient(#9aa6a6,#c9cfcc 45%,#4f7a35)" role="img" aria-label="Photo of a great wall over misty green mountains"></div>
<div class="tile" style="left:221px;top:960px;background:linear-gradient(#5b6f95,#a9b0b8 50%,#4c5159)" role="img" aria-label="Photo of industrial pipes and tanks"></div>
<div class="tile" style="left:376px;top:960px;background:linear-gradient(#5f93cf,#3f6ea6 55%,#2d3c52)" role="img" aria-label="Photo of glass office towers"></div>
<div class="tile" style="left:530px;top:960px;background:linear-gradient(#b9c9d8,#c6662f 55%,#3f6b35)" role="img" aria-label="Photo of a golden pagoda among trees"></div>

<footer class="site-footer">
  <div class="footer-col"><h4 style="left:69px">Quick Links</h4></div>
  <ul class="footer-links" style="left:69px"><li>Home</li><li>Services</li><li>Projects</li></ul>
  <ul class="footer-links" style="left:127px"><li>About Us</li><li>Blog</li><li>Contact us</li></ul>
  <ul class="footer-links" style="left:204px"><li>Help</li><li>Terms</li><li>Privacy</li></ul>
  <div class="footer-divider" style="left:268px"></div>
  <div class="footer-col"><h4 style="left:290px">Services</h4></div>
  <ul class="footer-links" style="left:291px"><li>Real Estate</li><li>Investment</li><li>Chain Management</li></ul>
  <ul class="footer-links" style="left:395px"><li>Real Estate</li><li>Investment</li><li>Chain Management</li></ul>
  <div class="footer-divider" style="left:488px"></div>
  <div class="footer-col"><h4 style="left:513px">Connect With Us</h4></div>
  <div class="social" style="left:513px;top:38px"><i></i>Circlebook</div>
  <div class="social" style="left:513px;top:59px"><i></i>Chirpline</div>
  <div class="social" style="left:610px;top:38px"><i></i>Worklink</div>
  <div class="social" style="left:610px;top:59px"><i></i>Clipstream</div>
</footer>
<div class="copyright">Copyright © 2013 VOSTREL HOLDINGS. All rights reserved.</div>

</div>
</body>
</html>
```